KRL Brochure

I'm looking to update and make easier to read our brochure. I uploaded our current brochure and logo.

Target Market(s)

Brides

Requirements
Must have
• same or similar text as in old brochure

```html
<!DOCTYPE html>
<html lang="en">
<head>
<meta charset="utf-8">
<title>KRL Video Brochure</title>
<link href="https://fonts.googleapis.com/css2?family=Cinzel:wght@400;700&family=Arimo&display=swap" rel="stylesheet">
<style>
:root{
  --panel-blue:rgba(78,88,170,.88);
  --column-blue:rgba(78,88,170,.72);
  --ink:#2b2118;
  --white:#ffffff;
  --band-blue:#5a64b0;
}
*{margin:0;padding:0;box-sizing:border-box}
html,body{width:1200px;height:927px;overflow:hidden;background:#fff}
.brochure{position:relative;width:1200px;height:927px;font-family:"Cinzel",serif;overflow:hidden}
.sunset-photo{position:absolute;left:0;top:0;width:800px;height:927px;
  background:linear-gradient(180deg,#8c86a2 0%,#b8a2a8 18%,#d8a88e 32%,#efb061 42%,#f4c25a 47%,#6f5440 56%,#3b3a30 66%,#2a2c24 100%)}
.garden-photo{position:absolute;left:800px;top:0;width:400px;height:672px;
  background:linear-gradient(180deg,#4a6a3a 0%,#6d7f5a 30%,#8a8270 45%,#6f8a4a 62%,#4d7a35 80%,#3e6a2c 100%)}
.garden-fade{position:absolute;left:800px;top:672px;width:400px;height:16px;background:#b8c9b4}
.badges{position:absolute;left:889px;top:44px;display:flex;gap:8px}
.badge{width:50px;height:50px;background:#f1e9c9}
.badge.round{border-radius:50%;background:#4fb7de}
.badge.tile{background:#6bb5d8}
.cover-brand{position:absolute;left:800px;top:688px;width:400px;height:222px;display:flex;align-items:center;justify-content:center}
.brand-name{font-weight:700;color:#3a3a3a;letter-spacing:2px}
.cover-brand .brand-name{font-size:48px}
.cover-band{position:absolute;left:800px;top:910px;width:400px;height:17px;background:var(--band-blue)}
.headline{position:absolute;left:63px;top:244px;color:var(--white);font-weight:700;font-size:23px;line-height:26px;letter-spacing:1px}
.headline .slowly{display:block;margin-top:26px}
.features{position:absolute;left:443px;top:38px;width:314px;text-align:center;color:var(--ink);list-style:none;font-size:18px;letter-spacing:1.5px}
.features li{line-height:22px}
.features .sep{font-size:11px;line-height:14px}
.mission{position:absolute;left:44px;top:403px;width:313px;height:480px;background:var(--panel-blue);color:var(--white);padding:24px 18px 0 19px;font-size:13.4px;line-height:15px;letter-spacing:.4px}
.mission p+p{margin-top:15px}
.contact{position:absolute;left:443px;top:470px;width:285px;height:457px;background:var(--column-blue);color:var(--white);text-align:center;font-size:14.5px;line-height:19px;letter-spacing:.5px}
.contact .brand-name{display:block;margin-top:126px;font-size:30px;color:#2b2f4a}
.contact address{font-style:normal;margin-top:20px}
.contact address p+p{margin-top:19px}
.credits{position:absolute;left:43px;top:893px;font-family:"Arimo",sans-serif;font-size:8.5px;line-height:11px;color:var(--white)}
</style>
</head>
<body>
<main class="brochure">
  <div class="sunset-photo" role="img" aria-label="Photo of a bride and groom kissing in silhouette before a lake at sunset"></div>
  <div class="garden-photo" role="img" aria-label="Photo of a couple kissing under a vine-covered pergola behind orange lilies"></div>
  <div class="garden-fade"></div>
  <div class="badges" aria-label="Award badges">
    <span class="badge"></span><span class="badge round"></span><span class="badge tile"></span><span class="badge tile"></span>
  </div>

  <h1 class="headline">Relive<br>the fastest day<br>of your life...<span class="slowly">Slowly</span></h1>

  <ul class="features">
    <li>Quality Digital Equipment</li><li class="sep">»«</li>
    <li>Unobtrusive</li><li class="sep">»«</li>
    <li>Professional Staff</li><li class="sep">»«</li>
    <li>Custom Packages</li><li class="sep">»«</li>
    <li>Photography Available</li><li class="sep">»«</li>
    <li>Aerial Video</li>
  </ul>

  <section class="mission">
    <p>Since 1995 our mission at KRL Video has been simple, to preserve the special moments of your wedding day in the most unobtrusive, discreet manner possible. Using hand held cameras and small lights allows us to blend in rather than stick out.</p>
    <p>We pride ourselves on personal service and going the extra mile for our clients. Each wedding is unique and our style reflects that individuality. We take personal pride in every video we create. We have thousands of satisfied clients who love our work and would recommend us to their closest friends and family.</p>
    <p>Video technology changes every day. We strive to stay ahead of the trend making sure you get a video you will enjoy just as much 20 years from now, as you do today.</p>
  </section>

  <section class="contact">
    <span class="brand-name">KRL Video</span>
    <address>
      <p>Alder Falls Office<br>48 Meadow Ln<br>Alder Falls, CT 06100</p>
      <p>Harbor Office<br>12 Pine St<br>Elmsford, CT 06123</p>
      <p>203-555-0148</p>
      <p>www.krlvideo.com</p>
    </address>
  </section>

  <p class="credits">Photo by Lakeside Photo Co.<br>All Major Credit Cards Accepted</p>

  <div class="cover-brand"><span class="brand-name">KRL Video</span></div>
  <div class="cover-band"></div>
</main>
</body>
</html>
```